Namecard Designs+Logo for a High End Automobile Company

We need a new business card for our company called Velta Motorhof.

www.veltamotorhof.example.sg
Our new website will be up in 2.5 months time.

We sell used and brand new continental cars like Korvane, QTL, Dravell, Solbrini and etc. Currently we are operating from 2 offices in Singapore and United Kingdom.

We want a design which is serious. We are open to colours but try to keep it at a maximum of 3 colours.

We prefer something simple and minimal. We are open to 2 sides printing or even 2 sided namecards. Both UK and Singapore company offices address must be in; either side by side, front and back, or even 2 sided cards.

The logo can be a text logo, emblem, abstract, pictorial or combination.

We are printing with Pribo.com so please kindly follow the printing guideline.

http://uk.pribo.example/help/faq/templates-and-guidelines.html

Rich and Car Enthusiasts

Printing

Must have
• Our 2 offices; UK and Singapore.

Our slogan which is " The Automobile Specialist"
Should not have
• Not more than 3 colours

```html
<!DOCTYPE html>
<html lang="en">
<head>
<meta charset="utf-8">
<title>Velta Motorhof – Business Card</title>
<link rel="stylesheet" href="https://fonts.googleapis.com/css2?family=Saira:ital,wght@0,400;0,600;1,400&family=Archivo+Black&family=Arimo:wght@400;700&display=swap">
<style>
  :root {
    --ink: #000000;
    --paper: #ffffff;
    --olive: #a5a92c;
    --olive-dark: #4b4a1c;
    --stage: #3a1c14;
  }
  * { margin: 0; padding: 0; box-sizing: border-box; }
  html, body { width: 1200px; height: 849px; overflow: hidden; }
  body { position: relative; background: var(--stage); font-family: "Arimo", Arial, sans-serif; }

  .brand-band { position: absolute; left: 0; top: 0; width: 1200px; height: 215px; background: var(--ink); }
  .brand-band .wordmark { position: absolute; left: 130px; top: 82px; font-size: 50px; }

  .wordmark {
    font-family: "Saira", Arial, sans-serif; font-weight: 600;
    color: var(--paper); letter-spacing: 0.5px; line-height: 1; white-space: nowrap;
  }

  .card { position: absolute; width: 545px; height: 302px; }

  .card-front { left: 62px; top: 428px; background: var(--ink); border-radius: 16px; }
  .card-front .slogan {
    position: absolute; right: 50px; top: 104px;
    font-family: "Arimo", Arial, sans-serif; font-weight: 700; font-size: 16px;
    letter-spacing: 1.6px; color: var(--olive); white-space: nowrap;
  }
  .card-front .wordmark { position: absolute; right: 50px; top: 130px; font-size: 46px; }

  .card-back { left: 592px; top: 403px; background: var(--paper); border-radius: 18px; overflow: hidden; }
  .holder { position: absolute; right: 59px; top: 38px; text-align: right; font-family: "Saira", Arial, sans-serif; }
  .holder-name { font-size: 26px; line-height: 1; color: var(--ink); font-weight: 400; }
  .holder-name b { font-weight: 600; }
  .holder-role { margin-top: 7px; font-size: 12px; font-style: italic; color: var(--olive); letter-spacing: 0.5px; }

  .divider { position: absolute; left: 0; right: 0; top: 95px; height: 18px; }
  .divider .rule { position: absolute; left: 0; right: 0; }
  .divider .rule-thin-a { top: 0; height: 2px; background: var(--olive); }
  .divider .rule-thin-b { top: 5px; height: 2px; background: var(--olive); }
  .divider .rule-bold { top: 10px; height: 6px; background: var(--olive-dark); }

  .office { position: absolute; top: 150px; font-size: 15px; line-height: 21px; }
  .office-sg { left: 56px; color: var(--ink); }
  .office-uk { left: 296px; color: var(--olive); }
  .office-name { font-family: "Archivo Black", Arial, sans-serif; font-size: 17px; margin-bottom: 25px; letter-spacing: 0.3px; }
</style>
</head>
<body>
  <header class="brand-band">
    <div class="wordmark">Velta Motorhof</div>
  </header>

  <section class="card card-front">
    <p class="slogan">THE AUTOMOBILE SPECIALIST</p>
    <div class="wordmark">Velta Motorhof</div>
  </section>

  <section class="card card-back">
    <div class="holder">
      <p class="holder-name">Marcus <b>Hale</b></p>
      <p class="holder-role">COMPANY DIRECTOR</p>
    </div>
    <div class="divider">
      <div class="rule rule-thin-a"></div>
      <div class="rule rule-thin-b"></div>
      <div class="rule rule-bold"></div>
    </div>
    <div class="office office-sg">
      <p class="office-name">singapore</p>
      <p>t. 020 746 464 64</p>
      <p>f. 020 839 393 93</p>
      <p>e. mh@veltamotorhof.example</p>
    </div>
    <div class="office office-uk">
      <p class="office-name">united kingdom</p>
      <p>t. 020 746 464 64</p>
      <p>f. 020 839 393 93</p>
      <p>e. mh@veltamotorhof.example</p>
    </div>
  </section>
</body>
</html>
```